Webdesign für Arbeitsschutz
Zielgruppe
Grundlage für ein funktionierendes Beschäftigungssystem ist die Schaffung und der Erhalt sicherer und menschengerechter Arbeitsbedingungen. Ein effizienter Arbeitsschutz und eine wirksame Unfallvermeidung sind hierfür besonders wichtig, vor allem auch im Hinblick auf die Herausforderungen einer durch digitalen Wandel immer schnelleren und anspruchsvolleren Arbeitswelt. Sicherheit und Gesundheit bei der Arbeit sind deshalb wichtige Arbeitsschwerpunkte im Landesamt für Betriebe und Sozialwesen. Ziel ist es, die Beschäftigten wirksam vor Gefahren und gesundheitlichen Schädigungen zu schützen. Verlässliche gesetzliche Grundlagen und rechtssichere Rahmenbedingungen für alle Unternehmen sind dafür unerlässlich.
Das wichtigste Grundlagengesetz für den betrieblichen Arbeitsschutz ist das Arbeitsschutzgesetz (ArbSchG). Es verpflichtet den Arbeitgeber, Gesundheitsgefährdungen am Arbeitsplatz zu beurteilen und über notwendige Schutzmaßnahmen zu entscheiden. Der Arbeitgeber hat für eine funktionierende Arbeitsschutzorganisation im Betrieb zu sorgen. Dies kann besonders wirksam durch eine nachhaltige Einbindung des Arbeits- und Gesundheitsschutzes in die Strukturen und Abläufe eines Unternehmens erreicht werden.
Aufgabenstellung
Gerne eine helle Seite mit schöner integration des Logo´s in die Homepage
Ich möchte keine exakte Kopie der Internet-Seite haben, aber alle Inhalte die Lemm-Arbeitsschutz anbietet (inkl. Rückrufservice, Anbringen von Referenz-Logos, Navigationsmenü)
Die Gestaltung der Hauptseite mit Farbe sollte bitte mit den vorhandenen Logo harmonieren. Die Aufteilung wo sich die Bausteine (Rückrufservice etc.) befindet sollte übersichtlich angebracht sein.

```html
<!DOCTYPE html>
<html lang="de">
<head>
<meta charset="utf-8">
<title>Arbeitsschutz &amp; Gesundheitsvorsorge Süd GmbH</title>
<link rel="stylesheet" href="https://fonts.googleapis.com/css2?family=Poppins:wght@300;400;500;600&display=swap">
<style>
:root{
  --teal:#336b80;
  --teal-dark:#2b5d70;
  --teal-band:#3b6e82;
  --ink:#333;
  --muted:#666;
  --light:#f7f7f7;
  --white:#fff;
  --line:#dcdcdc;
}
*{margin:0;padding:0;box-sizing:border-box}
html,body{width:1200px;height:3937px;overflow:hidden}
body{font-family:'Poppins',sans-serif;color:var(--ink);background:var(--white);position:relative}
.section{position:absolute;left:0;width:1200px}
.abs{position:absolute}

/* header */
.site-header{top:0;height:110px;border-bottom:2px solid var(--teal);background:var(--white)}
.brand{left:51px;top:16px;width:220px;text-align:center;color:var(--teal);font-size:10.5px;line-height:13px;white-space:nowrap}
.brand-square{display:block;width:34px;height:34px;border:3px solid var(--teal);margin:0 auto 8px}
.main-nav{left:416px;top:0;display:flex;height:76px}
.main-nav a{display:flex;align-items:flex-end;padding:0 8px 10px;font-size:10.5px;font-weight:500;color:var(--teal);text-decoration:none;white-space:nowrap}
.main-nav a.active{background:var(--teal);color:var(--white);padding:0 14px 10px}
.header-icons{left:1068px;top:43px;display:flex;gap:8px}
.header-icons span{width:30px;height:30px;background:var(--teal);display:flex;align-items:center;justify-content:center}

/* hero */
.hero{top:110px;height:613px}
.hero-photo{position:absolute;inset:0;background:linear-gradient(90deg,#b9c8d8 0%,#d6dde6 45%,#5f7fa8 62%,#3d5f8f 80%,#2e4a72 100%)}
.hero-panel{position:absolute;left:0;top:0}
.hero-title{left:61px;top:238px;font-size:40px;font-weight:600;line-height:50px;color:var(--white)}
.btn-outline{display:inline-flex;align-items:center;justify-content:center;border:1.5px solid var(--white);color:var(--white);font-size:13px}
.hero-btn{left:61px;top:387px;width:157px;height:37px}

/* section headings */
.sec-head{display:flex;align-items:flex-end;gap:10px}
.sec-head h2{font-size:17px;font-weight:500;letter-spacing:.5px;color:var(--ink)}
.sec-head .slash{font-size:26px;font-weight:300;color:var(--teal);line-height:24px}
.sec-head small{font-size:11.5px;color:var(--muted);transform:translateY(8px)}

/* services */
.services{top:723px;height:822px}
.service{width:290px}
.service h3{font-size:15px;font-weight:500;margin-bottom:16px}
.service p{font-size:14px;line-height:23px;color:#555;margin-bottom:6px}
.service a{display:inline-block;color:var(--teal);font-size:14px;text-decoration:none;padding-bottom:6px;border-bottom:1px solid #999}
.service.right{text-align:right}
.srv-icon{width:56px;height:56px}
.expert{left:450px;width:300px;text-align:center}
.expert-avatar{width:172px;height:172px;border-radius:50%;background:radial-gradient(circle at 50% 60%,#e8ecef 0 38%,var(--teal) 39%);margin:0 auto}
.expert p{margin-top:22px;font-size:15px;font-weight:500;line-height:25px;color:var(--teal)}

/* about */
.about{top:1545px;height:1073px;background:var(--light)}
.about-sub{left:0;width:1200px;top:138px;text-align:center;font-size:12px;line-height:21px;color:var(--teal)}
.about-title{left:0;width:1200px;top:336px;text-align:center;font-size:17px;font-weight:500;letter-spacing:.5px}
.info-box{background:var(--teal);color:var(--white);text-align:center;font-size:10px;line-height:21px;padding:18px 36px 0}
.info-box .btn-outline{width:125px;height:30px;font-size:10px;margin-top:14px;border-width:1px}
.box-main{left:434px;top:389px;width:306px;height:196px}
.box-left{left:92px;top:794px;width:306px;height:198px}
.box-right{left:803px;top:794px;width:306px;height:198px}
.pillar-title{width:360px;text-align:center;font-size:19px;font-weight:500}
.pillar-title small{display:block;font-size:12px;font-weight:400;color:var(--muted);margin-top:2px}

/* callback */
.callback{top:2618px;height:539px;background:var(--teal-band);color:var(--white)}
.callback h2{left:0;width:1200px;top:62px;text-align:center;font-size:18px;font-weight:500;letter-spacing:.5px}
.agent-photo{left:183px;top:142px;width:215px;height:397px;background:linear-gradient(180deg,#6f8797 0%,#4a5864 40%,#23262b 100%);border-radius:90px 90px 0 0}
.field{border-bottom:1px solid rgba(255,255,255,.7);font-size:12px;padding-bottom:14px;display:flex;justify-content:space-between}
.select{height:29px;background:var(--white);color:#666;font-size:10px;display:flex;align-items:center;justify-content:space-between;padding:0 12px}
.submit{left:670px;top:428px;width:157px;height:30px;background:#2a2f33;color:var(--white);font-size:13px;display:flex;align-items:center;justify-content:center}

/* references */
.refs{top:3157px;height:367px}
.ref-logo{width:220px;text-align:center;font-size:30px;font-weight:600;color:#2d2d2d}
.ref-arrows{left:570px;top:300px;display:flex;gap:10px;align-items:center;color:#444;font-size:12px}

/* footer */
.site-footer{top:3524px;height:413px;background:var(--light);border-top:1px solid #e4e4e4}
.footer-head{font-size:19px;font-weight:500;color:var(--teal);line-height:31px}
.contact-list{list-style:none;font-size:12px;color:#555}
.contact-list li{display:flex;align-items:center;gap:12px;height:25.5px}
.address{font-size:12px;color:#555;line-height:25px}
.address strong{font-weight:600;color:var(--ink);display:flex;gap:12px;align-items:center}
.foot-list{list-style:none;font-size:12px;color:#555}
.foot-list li{display:flex;align-items:center;gap:12px;height:24.5px}
.foot-list li::before{content:"";width:9px;height:9px;border:1px solid #777}
.footer-brand{left:380px;top:170px;width:440px;text-align:center;color:var(--teal);font-size:19px;line-height:24px;white-space:nowrap}
.footer-brand .brand-square{width:56px;height:56px;border-width:4px;margin-bottom:14px}
.copyright{left:0;top:372px;width:1200px;height:41px;background:var(--teal);color:var(--white);font-size:12px;font-weight:500;display:flex;align-items:center;justify-content:center}
</style>
</head>
<body>

<header class="section site-header">
  <div class="abs brand"><span class="brand-square"></span>Arbeitsschutz &amp; Gesundheitsvorsorge<br>Süd GmbH</div>
  <nav class="abs main-nav">
    <a class="active">Startseite</a><a>Beratung &amp; Betreuung</a><a>Seminare</a><a>E-Learning</a><a>Beauftragtenwesen</a><a>Das Unternehmen</a><a>Kontakt</a>
  </nav>
  <div class="abs header-icons">
    <span><svg width="13" height="10" viewBox="0 0 13 10"><rect x=".5" y=".5" width="12" height="9" fill="#fff"/><path d="M.5 .5 6.5 5.5 12.5 .5" stroke="#336b80" fill="none"/></svg></span>
    <span><svg width="13" height="13" viewBox="0 0 24 24"><path fill="#fff" d="M6.6 10.8a15 15 0 0 0 6.6 6.6l2.2-2.2c.3-.3.7-.4 1-.2 1.1.4 2.3.6 3.6.6.6 0 1 .4 1 1V20c0 .6-.4 1-1 1A17 17 0 0 1 3 4c0-.6.4-1 1-1h3.5c.6 0 1 .4 1 1 0 1.3.2 2.5.6 3.6.1.3 0 .7-.2 1z"/></svg></span>
  </div>
</header>

<section class="section hero">
  <div class="hero-photo" role="img" aria-label="Bauarbeiter mit orangefarbenem Schutzhelm vor einer Baustelle mit Kran"></div>
  <svg class="hero-panel" width="1200" height="613"><polygon points="0,25 527,219 359,613 0,613" fill="#336b80" fill-opacity=".88"/></svg>
  <h1 class="abs hero-title">Mit Sicherheit Mehr<br>Sicherheit</h1>
  <span class="abs btn-outline hero-btn">Mehr anzeigen</span>
</section>

<section class="section services">
  <div class="abs sec-head" style="left:407px;top:82px"><h2>DIENSTLEISTUNGEN</h2><span class="slash">/</span><small>Sie wissen, was wir anbieten</small></div>

  <svg class="abs srv-icon" style="left:61px;top:197px" viewBox="0 0 56 56" fill="none" stroke="#336b80" stroke-width="3"><circle cx="22" cy="16" r="10"/><path d="M4 48c0-11 8-18 18-18s18 7 18 18z"/><path d="M46 14v14M39 21h14"/></svg>
  <div class="abs service" style="left:148px;top:197px"><h3>Wir stellen ein</h3><p>Informieren Sie sich über<br>unsere Stellenangebote.</p><a>zu den Stellenausschreibungen</a></div>

  <svg class="abs srv-icon" style="left:61px;top:405px" viewBox="0 0 56 56" fill="none" stroke="#336b80" stroke-width="3"><path d="M22 4 4 10v14c0 12 8 20 18 24 10-4 18-12 18-24V10z"/><path d="m13 26 7 7 11-12"/></svg>
  <div class="abs service" style="left:148px;top:405px"><h3>Arbeitsschutz</h3><p>Sicherheit geht vor! Wir betreuen Ihr Unternehmen als externe Fachkraft für Arbeitssicherheit.</p><a>mehr zum Arbeitsschutz</a></div>

  <svg class="abs srv-icon" style="left:61px;top:603px" viewBox="0 0 56 56" fill="#336b80"><circle cx="9" cy="7" r="5"/><rect x="4" y="14" width="10" height="18"/><rect x="5" y="32" width="3" height="16"/><rect x="10" y="32" width="3" height="16"/><rect x="18" y="8" width="34" height="22" fill="none" stroke="#336b80" stroke-width="3"/><path d="M35 30 27 46M35 30l8 16" stroke="#336b80" stroke-width="3"/></svg>
  <div class="abs service" style="left:148px;top:603px"><h3>Seminare</h3><p>Wir bieten eine Vielzahl von fachspe-<br>zifischen Seminaren rund um den Arbeitsschutz.</p><a>Übersicht unserer Seminare</a></div>

  <div class="abs service right" style="left:763px;top:197px"><h3>E-Learning</h3><p>Sicherheitsunterweisungen online<br>mit E-Learning – flexibel,unkompliziert<br>und zeitsparend.</p><a>alles zum Thema E-Learning</a></div>
  <svg class="abs srv-icon" style="left:1080px;top:197px" viewBox="0 0 56 56" fill="none" stroke="#336b80" stroke-width="3"><rect x="8" y="8" width="40" height="28"/><path d="M2 42h52v4H2z"/></svg>

  <div class="abs service right" style="left:763px;top:405px"><h3>Beauftragtenwesen</h3><p>Übernahme der Beauftragten Funkt-<br>ionen – von Gefahrstoffen bis hin<br>zum Brandschutz.</p><a>mehr zum Beauftragtenwesen</a></div>
  <svg class="abs srv-icon" style="left:1080px;top:405px" viewBox="0 0 56 56" fill="none" stroke="#336b80" stroke-width="3"><path d="M18 30V10m8 20V6m8 24V8m8 24V14M18 30c-4-4-8-2-6 2l10 14c2 4 6 6 12 6 8 0 8-8 8-12V30"/></svg>

  <div class="abs service right" style="left:763px;top:603px"><h3>StoffA - Gefahrstoff Softwarelösung</h3><p>Gefahrstoff-Management, einfach wie<br>nie zuvor! Flexibel und anpas-sbar<br>an Ihre Prozesse.</p><a>mehr zu StoffA</a></div>
  <svg class="abs srv-icon" style="left:1080px;top:603px" viewBox="0 0 56 56" fill="none" stroke="#336b80" stroke-width="3"><rect x="18" y="6" width="34" height="24"/><path d="M4 34h16l8 4h14v6H22L4 48z" fill="#336b80"/></svg>

  <div class="abs expert" style="top:341px">
    <div class="expert-avatar" role="img" aria-label="Illustration eines Sachverständigen in Uniform mit Mütze"></div>
    <p>Ihr Ingenieur- und Sachver-<br>ständigenbüro für Arbeitssi-<br>cherheit</p>
  </div>
</section>

<section class="section about">
  <div class="abs sec-head" style="left:496px;top:83px"><h2>ÜBER UNS</h2><span class="slash">/</span><small>unsere Arbeit</small></div>
  <p class="abs about-sub">Ihr Ingenieur- und Sachverständigenbüro für<br>Arbeitssicherheit</p>
  <svg class="abs" style="left:564px;top:242px" width="48" height="58" viewBox="0 0 48 58" fill="none" stroke="#336b80" stroke-width="4"><path d="M24 3 4 10v17c0 14 9 23 20 28 11-5 20-14 20-28V10z"/><path d="m13 29 8 8 14-15"/></svg>
  <h2 class="abs about-title">IHRE SICHERHEIT IST UNSERE AUFGABE!</h2>

  <div class="abs info-box box-main">Die Implementierung des Arbeits- und Gesundheitsschutzes ist für alle Betriebe egal in welcher Größe und Branche ein wichtiges Thema, denn der Gesetzgeber verpflichtet Unternehmen zur Umsetzung der<br><span class="btn-outline">Lesen Sie mehr</span></div>

  <svg class="abs" style="left:0;top:0" width="1200" height="1073" fill="none" stroke="#555" stroke-width="1" stroke-dasharray="5 4"><path d="M555 611 433 794M645 611 769 794M451 889H749"/></svg>

  <svg class="abs" style="left:214px;top:658px" width="62" height="48" viewBox="0 0 62 48"><path d="M8 34C8 14 18 4 32 4s24 10 24 30z" fill="#336b80"/><path d="M2 38c14 8 44 8 58-4l-4-4C42 40 16 40 4 32z" fill="#336b80"/></svg>
  <div class="abs pillar-title" style="left:65px;top:735px">Lemm Arbeitsschutz</div>
  <div class="abs info-box box-left">Lemm Arbeitsschutz ist Ihr zertifizierter Dienstleister für den Raum Karlsruhe und die Region Rhein-Neckar, wenn es um die betriebliche Sicherheit geht.Wir bieten unseren Kunden als externe<br><span class="btn-outline">Lesen Sie mehr</span></div>

  <svg class="abs" style="left:933px;top:654px" width="46" height="48" viewBox="0 0 46 48" fill="#336b80"><circle cx="19" cy="12" r="10"/><path d="M2 46c0-14 8-20 17-20 6 0 10 2 13 6v14z"/><path d="M36 28 28 31v7c0 5 3 8 8 10 5-2 8-5 8-10v-7z"/></svg>
  <div class="abs pillar-title" style="left:776px;top:735px">Fachkraft für Arbeitssicherheit<small>(SiFa, FaSi)</small></div>
  <div class="abs info-box box-right">Wir unterstützen Sie als Fachkraft für Arbeitssicherheit bei der Erstellung der Gefährdungsbeurteilung, den regelmäßigen Betriebsbegehungen sowie bei den jährlichen Sicherheitsunterweisungen<br><span class="btn-outline">Lesen Sie mehr</span></div>
</section>

<section class="section callback">
  <h2 class="abs">UNSER RÜCKRUFSERVICE</h2>
  <div class="abs agent-photo" role="img" aria-label="Foto einer Beraterin im dunklen Blazer mit Mappe"></div>

  <div class="abs field" style="left:479px;top:180px;width:156px"><span>Anrede*</span><svg width="10" height="8"><path d="M1 2l4 4 4-4" stroke="#fff" stroke-width="2" fill="none"/></svg></div>
  <div class="abs field" style="left:668px;top:180px;width:158px"><span>Name *</span></div>
  <div class="abs field" style="left:859px;top:180px;width:158px"><span>Vorname *</span></div>
  <div class="abs field" style="left:479px;top:241px;width:273px"><span>Firma *</span></div>
  <div class="abs field" style="left:790px;top:241px;width:227px"><span style="padding-left:69px">Telefonnr. *</span></div>
  <div class="abs field" style="left:479px;top:295px;width:538px"><span>Betreff *</span></div>

  <div class="abs select" style="left:547px;top:359px;width:126px"><span>Wochentag:</span><svg width="10" height="8"><path d="M1 2l4 4 4-4" stroke="#333" stroke-width="2" fill="none"/></svg></div>
  <div class="abs select" style="left:685px;top:359px;width:125px"><span>Wochentag:</span><svg width="10" height="8"><path d="M1 2l4 4 4-4" stroke="#333" stroke-width="2" fill="none"/></svg></div>
  <div class="abs select" style="left:823px;top:359px;width:125px"><span>Wochentag:</span><svg width="10" height="8"><path d="M1 2l4 4 4-4" stroke="#333" stroke-width="2" fill="none"/></svg></div>
  <div class="abs submit">absenden</div>
</section>

<section class="section refs">
  <div class="abs sec-head" style="left:333px;top:80px"><h2>AUSZUG AUS UNSEREN REFERENZEN</h2><span class="slash">/</span><small>die besten Dienstleistungen</small></div>
  <div class="abs ref-logo" style="left:63px;top:208px">Sonnhof</div>
  <div class="abs ref-logo" style="left:346px;top:208px">KRAVELL</div>
  <div class="abs ref-logo" style="left:632px;top:208px">LOREVO</div>
  <div class="abs ref-logo" style="left:919px;top:208px">DANTRIX</div>
  <div class="abs ref-arrows">
    <svg width="12" height="20"><path d="M10 2 2 10l8 8" stroke="#444" stroke-width="2.5" fill="none"/></svg><span>|</span><svg width="12" height="20"><path d="M2 2l8 8-8 8" stroke="#444" stroke-width="2.5" fill="none"/></svg>
  </div>
</section>

<footer class="section site-footer">
  <h3 class="abs footer-head" style="left:64px;top:62px">Zögern Sie nicht, kontaktieren<br>Sie uns.</h3>
  <ul class="abs contact-list" style="left:64px;top:136px">
    <li><svg width="12" height="12" viewBox="0 0 24 24"><path fill="#333" d="M6.6 10.8a15 15 0 0 0 6.6 6.6l2.2-2.2c.3-.3.7-.4 1-.2 1.1.4 2.3.6 3.6.6.6 0 1 .4 1 1V20c0 .6-.4 1-1 1A17 17 0 0 1 3 4c0-.6.4-1 1-1h3.5c.6 0 1 .4 1 1 0 1.3.2 2.5.6 3.6.1.3 0 .7-.2 1z"/></svg>+49 7231 55820 - 0</li>
    <li><svg width="12" height="12" viewBox="0 0 24 24"><path fill="#333" d="M6.6 10.8a15 15 0 0 0 6.6 6.6l2.2-2.2c.3-.3.7-.4 1-.2 1.1.4 2.3.6 3.6.6.6 0 1 .4 1 1V20c0 .6-.4 1-1 1A17 17 0 0 1 3 4c0-.6.4-1 1-1h3.5c.6 0 1 .4 1 1 0 1.3.2 2.5.6 3.6.1.3 0 .7-.2 1z"/></svg>+49 7231 55820 - 19</li>
    <li><svg width="12" height="10" viewBox="0 0 13 10"><rect width="13" height="10" fill="#333"/><path d="M0 0 6.5 5.5 13 0" stroke="#f7f7f7" fill="none"/></svg>info(at)lemm-arbeitsschutz.de</li>
    <li><svg width="12" height="12" viewBox="0 0 12 12" fill="none" stroke="#333"><circle cx="6" cy="6" r="5"/><path d="M1 6h10M6 1c-3 3-3 7 0 10M6 1c3 3 3 7 0 10"/></svg>www.lemm-arbeitsschutz.de</li>
  </ul>
  <div class="abs address" style="left:64px;top:262px">
    <strong><svg width="10" height="14" viewBox="0 0 10 14"><path fill="#333" d="M5 0a5 5 0 0 0-5 5c0 4 5 9 5 9s5-5 5-9a5 5 0 0 0-5-5zm0 7a2 2 0 1 1 0-4 2 2 0 0 1 0 4z"/></svg>LEMM ARBEITSSCHUTZ GMBH &amp; CO. KG</strong>
    <div style="padding-left:20px">Lindenweg 14<br>75179 Talheim</div>
  </div>

  <div class="abs footer-brand"><span class="brand-square"></span>Arbeitsschutz &amp; Gesundheitsvorsorge<br>Süd GmbH</div>

  <h3 class="abs footer-head" style="left:933px;top:56px">Software</h3>
  <ul class="abs foot-list" style="left:933px;top:106px"><li>E-Learning</li><li>Gefahrstoff-Software StoffA</li></ul>
  <h3 class="abs footer-head" style="left:938px;top:184px">Software</h3>
  <ul class="abs foot-list" style="left:938px;top:234px"><li>Impressum</li><li>Datenschutz</li><li>Netzwerk</li><li>Jobs</li></ul>

  <div class="abs copyright">Copyright 2015 www.lemm-arbeitsschutz.de</div>
</footer>

</body>
</html>
```